Wedding Videography Wordpress Website Theme

We need a modern and high-end website look for our wedding video and film business. We film weddings all over the United Kingdom and at European destinations so need something to reflect our work. The website should be visually stunning with images and videos being the focal point as this is what our services are.

The current website is www.brennolfside.com so you will be able to see our brand.

My Instagram is www.instagram.com/brennolfsidefilms so a new design should link in with this idea.

We need the following pages designed by the winning designer

1 - Homepage
2 - Films Index Page
3 - Testimonials
4 - Prices
5 - Reviews
6 - Meet Corin (About)
7 - Contact
8 - Blog Index
9 - Blog Page

All pages must be consistent so have a similar style.

Pages on menu:
Meet Corin
Videos
Packages
Testimionials
Journal (Blog)
Contact

We require a responsive look too. Over 90% of our visitors access the website via their mobile devices.

```html
<!DOCTYPE html>
<html lang="en">
<head>
<meta charset="utf-8">
<title>Corin Brennolfside – Wedding Films</title>
<link rel="stylesheet" href="https://fonts.googleapis.com/css2?family=Playfair+Display:wght@400;700;900&family=Montserrat:wght@400;500;600&display=swap">
<style>
:root{
  --gold:#c9a13b;
  --gold-light:#f6dea0;
  --cream:#efe3c4;
  --ink:#1d1c18;
  --brown:#3a2e10;
  --paper:#edebe8;
  --white:#ffffff;
  --text-dark:#3a3a3a;
  --serif:'Playfair Display', Georgia, serif;
  --sans:'Montserrat', Arial, sans-serif;
}
*{box-sizing:border-box;margin:0;padding:0}
html,body{width:1200px;height:3896px;overflow:hidden}
body{position:relative;background:var(--white);font-family:var(--sans);color:var(--text-dark)}
.abs{position:absolute}

/* Header & hero */
.hero{left:0;top:0;width:1200px;height:710px;
  background:
    radial-gradient(ellipse 170px 230px at 600px 250px,rgba(214,190,130,.55),rgba(214,190,130,0) 100%),
    radial-gradient(ellipse 260px 260px at 600px 220px,rgba(120,110,60,.55),rgba(120,110,60,0) 100%),
    radial-gradient(ellipse 150px 120px at 480px 140px,rgba(150,140,70,.45),rgba(150,140,70,0) 100%),
    radial-gradient(ellipse 150px 140px at 730px 150px,rgba(130,120,60,.45),rgba(130,120,60,0) 100%),
    radial-gradient(ellipse 700px 260px at 560px 540px,rgba(88,92,48,.75),rgba(88,92,48,0) 100%),
    radial-gradient(ellipse 60px 40px at 170px 650px,rgba(230,150,60,.45),rgba(230,150,60,0) 100%),
    radial-gradient(ellipse 50px 35px at 1135px 600px,rgba(230,150,60,.45),rgba(230,150,60,0) 100%),
    radial-gradient(ellipse 50px 35px at 920px 450px,rgba(230,150,60,.35),rgba(230,150,60,0) 100%),
    linear-gradient(180deg,#1b1a15 0%,#2a281d 45%,#3a3a24 80%,#252417 100%)}
.brand{color:var(--white);font-family:var(--sans);font-weight:600;text-align:center;letter-spacing:3px;line-height:1.3;white-space:nowrap}
.brand-header{left:100px;top:64px;font-size:12px;width:160px}
.brand small{display:block;font-size:7px;letter-spacing:3px}
.nav{left:487px;top:49px;display:flex;gap:24px;font-family:var(--serif);font-weight:700;font-size:13px;color:var(--white);white-space:nowrap}
.social{display:flex;gap:10px}
.social span{width:20px;height:20px;border-radius:50%;background:var(--gold);display:block}
.social-header{left:1034px;top:48px}
.hero-frame{left:231px;top:421px;width:736px;height:104px;border:1.5px solid var(--gold-light)}
.hero-title{left:0;top:366px;width:1200px;text-align:center;font-family:var(--serif);font-weight:900;font-size:78px;color:var(--white);line-height:1;white-space:nowrap}
.hero-sub{left:0;top:460px;width:1200px;text-align:center;font-size:17px;color:var(--white)}
.play{width:54px;height:54px}
.hero-play{left:572px;top:492px}
.dots{left:558px;top:573px;display:flex;gap:7px}
.dots i{width:15px;height:15px;border-radius:50%;border:2px solid var(--white);display:block}
.dots i:first-child{background:var(--gold)}

/* Section headings */
.section-title{left:0;width:1200px;text-align:center;font-family:var(--serif);font-weight:700;font-size:40px;letter-spacing:17px;color:var(--gold);white-space:nowrap}

/* Videos */
.video-card{top:890px;width:476px;height:370px;box-shadow:0 2px 8px rgba(0,0,0,.12)}
.video-thumb{width:100%;height:295px;position:relative}
.video-thumb .play{position:absolute;left:211px;top:121px}
.video-caption{height:75px;display:flex;align-items:center}
.video-caption .couple{width:174px;text-align:center;font-family:var(--serif);font-weight:700;font-size:13px;letter-spacing:1px;border-right:1px solid rgba(0,0,0,.15);height:100%;display:flex;align-items:center;justify-content:center;white-space:nowrap}
.video-caption .place{padding-left:22px;font-size:14px;line-height:1.35}
.card-one .video-thumb{background:
  radial-gradient(ellipse 80px 130px at 240px 190px,rgba(240,236,226,.75),rgba(240,236,226,0) 100%),
  radial-gradient(ellipse 60px 130px at 150px 170px,rgba(30,30,30,.7),rgba(30,30,30,0) 100%),
  radial-gradient(ellipse 30px 30px at 185px 190px,rgba(170,20,40,.8),rgba(170,20,40,0) 100%),
  linear-gradient(180deg,#a9a28e 0%,#8d8671 30%,#66703f 58%,#75843f 100%)}
.card-one .video-caption{background:var(--gold-light);color:var(--ink)}
.card-two .video-thumb{background:
  radial-gradient(ellipse 90px 140px at 330px 200px,rgba(220,220,220,.6),rgba(220,220,220,0) 100%),
  radial-gradient(ellipse 70px 160px at 200px 160px,rgba(20,20,20,.75),rgba(20,20,20,0) 100%),
  linear-gradient(90deg,#8c8c8c 0%,#6a6a6a 30%,#3e3e3e 60%,#555 100%)}
.card-two .video-caption{background:var(--gold);color:var(--white)}
.card-two .couple{border-right-color:rgba(255,255,255,.4)}
.btn{display:flex;align-items:center;justify-content:center;font-family:var(--serif);font-weight:700;white-space:nowrap}
.btn-more-video{left:496px;top:1300px;width:208px;height:42px;background:var(--cream);color:var(--ink);font-size:14px}

/* Meet */
.meet{left:0;top:1450px;width:1200px;height:718px;background:
  radial-gradient(ellipse 300px 200px at 200px 120px,rgba(60,66,50,.55),rgba(60,66,50,0) 100%),
  radial-gradient(ellipse 260px 220px at 650px 500px,rgba(58,62,48,.55),rgba(58,62,48,0) 100%),
  radial-gradient(ellipse 300px 260px at 1080px 200px,rgba(52,56,44,.5),rgba(52,56,44,0) 100%),
  radial-gradient(ellipse 320px 200px at 300px 620px,rgba(50,54,42,.5),rgba(50,54,42,0) 100%),
  linear-gradient(90deg,#16160f,#22221b 55%,#1a1a14)}
.meet-title{left:109px;top:1568px;font-family:var(--serif);font-weight:700;font-size:40px;letter-spacing:14px;color:var(--gold);white-space:nowrap}
.meet-copy{left:109px;top:1632px;width:478px;font-size:13.5px;line-height:24.3px;color:var(--white);text-align:justify}
.meet-copy p{margin-bottom:24px}
.btn-meet{left:109px;top:2005px;width:207px;height:42px;background:var(--gold);color:var(--ink);font-size:14px}
.meet-photo{left:670px;top:1577px;width:348px;height:473px;background:
  radial-gradient(ellipse 60px 70px at 120px 110px,rgba(200,160,130,.55),rgba(200,160,130,0) 100%),
  radial-gradient(ellipse 110px 260px at 290px 300px,rgba(225,220,212,.6),rgba(225,220,212,0) 100%),
  radial-gradient(ellipse 110px 220px at 120px 340px,rgba(45,50,58,.8),rgba(45,50,58,0) 100%),
  linear-gradient(160deg,#5a4c40 0%,#3e3a34 55%,#2c2a26 100%)}

/* Newsletter */
.newsletter{left:0;top:2168px;width:1200px;height:519px;background:
  radial-gradient(ellipse 180px 260px at 630px 330px,rgba(255,255,255,.6),rgba(255,255,255,0) 100%),
  radial-gradient(ellipse 400px 200px at 250px 150px,rgba(222,216,206,.7),rgba(222,216,206,0) 100%),
  radial-gradient(ellipse 400px 220px at 1000px 380px,rgba(220,214,204,.7),rgba(220,214,204,0) 100%),
  linear-gradient(180deg,#ecebe8,#e6e3de)}
.news-text{left:0;top:2339px;width:1200px;text-align:center;font-size:22px;line-height:33px;color:var(--text-dark)}
.news-input{left:336px;top:2437px;width:525px;height:66px;background:#ecdcb0;color:#9a8d6a;font-size:15px;padding-left:22px;display:flex;align-items:center}
.btn-subscribe{left:336px;top:2513px;width:527px;height:65px;background:var(--gold);color:var(--white);font-size:24px}

/* Gallery */
.gallery-item{top:2687px;width:284px;height:232px}

/* Contact */
.contact-gold{left:0;top:2931px;width:1200px;height:367px;background:
  radial-gradient(ellipse 500px 120px at 600px 20px,rgba(230,200,110,.5),rgba(230,200,110,0) 100%),
  var(--gold)}
.contact-dark{left:0;top:3298px;width:1200px;height:598px;background:var(--brown)}
.contact-title{color:var(--ink);top:2990px}
.contact-intro{left:0;top:3053px;width:1200px;text-align:center;font-size:15px;line-height:21.5px;color:#6b5212}
.contact-card{left:110px;top:3124px;width:978px;height:412px;background:var(--white)}
.icon-mail{left:146px;top:3165px;width:48px;height:48px}
.touch-eyebrow{left:146px;top:3236px;font-size:21px;letter-spacing:3px;color:var(--ink);white-space:nowrap}
.touch-title{left:146px;top:3268px;font-size:30px;font-weight:600;color:var(--ink);white-space:nowrap}
.touch-text{left:146px;top:3316px;width:420px;font-size:15px;line-height:21px;color:#8b8b8b}
.contact-line{left:152px;font-size:18px;color:var(--gold);display:flex;align-items:center;gap:8px;white-space:nowrap}
.field{height:39px;border:1px solid #cfcfcf;font-size:10.5px;color:#9a9a9a;padding:0 12px 0 16px;display:flex;align-items:center;letter-spacing:.5px;white-space:nowrap}
.field-area{align-items:flex-start;padding-top:14px}
.field-date{justify-content:space-between}
.btn-submit{left:587px;top:3431px;width:242px;height:49px;background:var(--gold);color:var(--ink);font-size:17px}

/* Footer */
.brand-footer{left:110px;top:3682px;font-size:19px;width:210px;letter-spacing:4px}
.brand-footer small{font-size:9px;letter-spacing:5px}
.footer-links{left:0;top:3749px;width:1200px;text-align:center;font-size:12px;color:var(--white);white-space:nowrap}
.footer-links span{margin:0 9px}
.copyright{left:0;top:3782px;width:1200px;text-align:center;font-size:12px;color:var(--white)}
.social-footer{left:574px;top:3818px}
</style>
</head>
<body>

<!-- Hero -->
<div class="abs hero" role="img" aria-label="Couple embracing under a floral arch at night with glowing lanterns on the lawn"></div>
<div class="abs brand brand-header">BRENNOLFSIDE<small>WEDDING FILMS</small></div>
<nav class="abs nav"><span>Home</span><span>Meet Corin</span><span>Videos</span><span>Packages</span><span>Testimonials</span><span>Journal</span><span>Contact</span></nav>
<div class="abs social social-header"><span></span><span></span></div>
<div class="abs hero-frame"></div>
<h1 class="abs hero-title">Corin Brennolfside</h1>
<p class="abs hero-sub">North East and Yorkshire Wedding Videographer</p>
<svg class="abs play hero-play" viewBox="0 0 54 54"><circle cx="27" cy="27" r="24" fill="rgba(0,0,0,.3)" stroke="#c9a13b" stroke-width="3"/><path d="M21 16 L38 27 L21 38 Z" fill="none" stroke="#c9a13b" stroke-width="3" stroke-linejoin="round"/></svg>
<div class="abs dots"><i></i><i></i><i></i><i></i></div>
<svg class="abs" style="left:0;top:690px" width="1200" height="50" viewBox="0 0 1200 50"><polygon points="0,8 1200,10 1200,28 0,48" fill="#c9a13b"/></svg>

<!-- Videos -->
<h2 class="abs section-title" style="top:815px">OUR VIDEOS</h2>
<article class="abs video-card card-one" style="left:112px">
  <div class="video-thumb" role="img" aria-label="Bride and groom laughing on a lawn before a stately stone house">
    <svg class="play" viewBox="0 0 54 54"><circle cx="27" cy="27" r="17" fill="none" stroke="#fff" stroke-width="2.5"/><path d="M23 19 L34 27 L23 35 Z" fill="none" stroke="#fff" stroke-width="2.5" stroke-linejoin="round"/></svg>
  </div>
  <div class="video-caption"><div class="couple">ELOWEN + TOMAS</div><div class="place">North East, UK and<br>Destination</div></div>
</article>
<article class="abs video-card card-two" style="left:611px">
  <div class="video-thumb" role="img" aria-label="Black and white shot of the couple dancing">
    <svg class="play" viewBox="0 0 54 54"><circle cx="27" cy="27" r="17" fill="none" stroke="#c9a13b" stroke-width="2.5"/><path d="M23 19 L34 27 L23 35 Z" fill="none" stroke="#c9a13b" stroke-width="2.5" stroke-linejoin="round"/></svg>
  </div>
  <div class="video-caption"><div class="couple">ELOWEN + TOMAS</div><div class="place">North East, UK and<br>Destination</div></div>
</article>
<div class="abs btn btn-more-video">View More Video</div>

<!-- Meet -->
<div class="abs meet" role="img" aria-label="Dark foliage background"></div>
<svg class="abs" style="left:0;top:1425px" width="1200" height="50" viewBox="0 0 1200 50"><polygon points="0,22 1200,4 1200,45 0,35" fill="#c9a13b"/><polygon points="0,35 1200,45 1200,50 0,50" fill="#1a1a14"/></svg>
<h2 class="abs meet-title">MEET CORIN</h2>
<div class="abs meet-copy">
  <p>Thanks so much for exploring my website. I hope you’ve had a chance to watch some of the gorgeous wedding films and you’ve enjoyed seeing the kind of high-quality, professional wedding video you could expect too.</p>
  <p>Videomaking has been a passion since I was eight years old. From making family videos, I went on to study video at college and then at degree level. You could say it’s second nature to me by now – I’ve been honing my filmmaking skills for years!</p>
  <p>When I’m not behind a camera, I love spending quality time with my two children (have you seen our family videos here?). We’re usually on an adventure somewhere, having fun. Life’s for making memories, right? And making sure we never forget the little details.</p>
</div>
<div class="abs btn btn-meet">View More</div>
<div class="abs meet-photo" role="img" aria-label="Smiling groom beside his bride at the ceremony"></div>

<!-- Newsletter -->
<div class="abs newsletter" role="img" aria-label="Faded wedding scene background"></div>
<h2 class="abs section-title" style="top:2264px">JOIN OUR NEWSLETTER</h2>
<p class="abs news-text">Subscribe to our mailing list to receive updates<br>and promotional offers.</p>
<div class="abs news-input">Enter your E - mail</div>
<div class="abs btn btn-subscribe">SUBSCRIBE</div>

<!-- Gallery -->
<div class="abs gallery-item" style="left:11px;background:radial-gradient(ellipse 70px 110px at 200px 150px,rgba(245,242,236,.8),rgba(245,242,236,0) 100%),radial-gradient(ellipse 70px 120px at 80px 170px,rgba(25,25,30,.85),rgba(25,25,30,0) 100%),linear-gradient(180deg,#5f7240,#8c9a6a 45%,#4e5a38)" role="img" aria-label="Couple laughing among greenery"></div>
<div class="abs gallery-item" style="left:309px;background:linear-gradient(180deg,#4a4448 0%,#6e6260 40%,#fff 40.5%,#fff 41%,#6c5858 41.5%,#b59a9c 75%,#c8b2b4 100%)" role="img" aria-label="Bridal preparations collage"></div>
<div class="abs gallery-item" style="left:607px;background:radial-gradient(ellipse 140px 70px at 142px 150px,rgba(235,225,215,.85),rgba(235,225,215,0) 100%),linear-gradient(180deg,#8f9592 0%,#a6a8a0 35%,#c9bcae 65%,#8a8678 100%)" role="img" aria-label="Bridesmaids cheering with bouquets"></div>
<div class="abs gallery-item" style="left:905px;background:radial-gradient(ellipse 40px 90px at 140px 150px,rgba(235,230,222,.8),rgba(235,230,222,0) 100%),radial-gradient(ellipse 160px 80px at 142px 40px,rgba(220,170,90,.5),rgba(220,170,90,0) 100%),linear-gradient(180deg,#4a3a28,#2e2720 60%,#1f1c18)" role="img" aria-label="Bride and family under fairy lights"></div>

<!-- Contact -->
<div class="abs contact-gold"></div>
<div class="abs contact-dark"></div>
<h2 class="abs section-title contact-title">CONTACT US</h2>
<p class="abs contact-intro">Before enquiring please check my prices to see if I am within your budget.<br>Click here for my packages. We can chat about your wedding plans, check my availability, and<br>see if we’re a match made in heaven.</p>
<div class="abs contact-card"></div>
<svg class="abs icon-mail" viewBox="0 0 48 48"><path d="M4 20 L24 6 L44 20 V44 H4 Z" fill="#f6dea0" stroke="#c9a13b" stroke-width="2.5" stroke-linejoin="round"/><rect x="11" y="12" width="26" height="18" fill="#fff" stroke="#c9a13b" stroke-width="2"/><path d="M16 18 H32 M16 23 H32" stroke="#c9a13b" stroke-width="2"/><path d="M4 20 L24 34 L44 20" fill="none" stroke="#c9a13b" stroke-width="2.5"/></svg>
<div class="abs touch-eyebrow">GET IN TOUCH</div>
<div class="abs touch-title">READY FOR A CHAT?</div>
<p class="abs touch-text">Neque porro quisquam est qui dolorem<br>ipsum quia dolor sit amet, consectetur, adipisci velit...</p>
<div class="abs contact-line" style="top:3423px"><svg width="18" height="18" viewBox="0 0 24 24"><path d="M6.6 10.8a15 15 0 0 0 6.6 6.6l2.2-2.2a1 1 0 0 1 1-.25 11.4 11.4 0 0 0 3.6.57 1 1 0 0 1 1 1V20a1 1 0 0 1-1 1A17 17 0 0 1 3 4a1 1 0 0 1 1-1h3.5a1 1 0 0 1 1 1c0 1.25.2 2.45.57 3.57a1 1 0 0 1-.25 1Z" fill="#c9a13b"/></svg>| &nbsp;+07700 900 318</div>
<div class="abs contact-line" style="top:3458px"><svg width="18" height="18" viewBox="0 0 24 24"><rect x="2" y="5" width="20" height="14" rx="1" fill="#c9a13b"/><path d="M2 6 L12 13 L22 6" fill="none" stroke="#fff" stroke-width="1.6"/></svg>| &nbsp;+films@brennolfside.com</div>
<div class="abs field" style="left:590px;top:3164px;width:227px">NAME</div>
<div class="abs field" style="left:825px;top:3164px;width:227px">PHONE</div>
<div class="abs field" style="left:590px;top:3232px;width:227px">EMAIL</div>
<div class="abs field field-date" style="left:825px;top:3232px;width:227px">WHEN IS YOUR WEDDING DAY?<svg width="10" height="10" viewBox="0 0 10 10"><rect x="0.5" y="1.5" width="9" height="8" fill="#9a9a9a"/></svg></div>
<div class="abs field field-area" style="left:590px;top:3298px;width:462px;height:114px">WHAT TIME IS YOUR WEDDING CEREMONY?</div>
<div class="abs btn btn-submit">SUBMIT NOW</div>

<!-- Footer -->
<div class="abs brand brand-footer">BRENNOLFSIDE<small>WEDDING FILMS</small></div>
<div class="abs" style="left:490px;top:3610px;width:96px;height:96px;border-radius:18px;background:#c23a7a" role="img" aria-label="Regional finalist award badge"></div>
<div class="abs" style="left:600px;top:3672px;width:110px;height:40px;border-radius:4px;background:#b8306e"></div>
<div class="abs brand" style="left:837px;top:3666px;width:118px;font-size:10px;letter-spacing:2px">BRENNOLFSIDE<small>WEDDING FILMS</small></div>
<div class="abs" style="left:965px;top:3625px;width:50px;height:62px;background:#e8e8ee" role="img" aria-label="Accreditation badge"></div>
<div class="abs" style="left:1020px;top:3622px;width:67px;height:67px;border-radius:50%;background:var(--gold-light)" role="img" aria-label="Featured listing badge"></div>
<div class="abs footer-links"><span>FAQ’s</span>|<span>Wedding Photography</span>|<span>Commercial</span>|<span>North East Wedding Venues</span>|<span>Free Speeches Guide</span>|<span>Blog</span></div>
<div class="abs copyright">© COPYRIGHT 2022 BRENNOLFSIDE FILMS LTD. ALL RIGHTS RESERVED</div>
<div class="abs social social-footer"><span></span><span></span></div>

</body>
</html>
```